Garnett and Lyle Personal Injury Billboard

We'd like a clean/modern billboard to build brand awareness for our law firm in the area of personal injury. Ideally, we like the word "Injured?" or something similar in large lettering.

I'm attaching images, logo and award badges which could be used. The billboards will be 14x48 ft and 10.6x36.

We are open to different color ideas, fonts, and artwork. Creative but not too busy with wording. Our web page is www.kgarnettfirm.example

Garnett & Lyle Law Firm
(555) 318-4092

```html
<!DOCTYPE html>
<html lang="en">
<head>
<meta charset="utf-8">
<title>Garnett &amp; Lyle Personal Injury Billboard</title>
<link rel="stylesheet" href="https://fonts.googleapis.com/css2?family=Alfa+Slab+One&family=Open+Sans:wght@700;800&family=Montserrat:wght@700&display=swap">
<style>
  :root {
    --ink: #111111;
    --paper: #ffffff;
    --paper-soft: #f4f4f4;
    --accent-red: #ee1c1c;
    --accent-blue: #0aa6e8;
    --badge-navy: #1d2430;
    --photo-warm: #8a6a52;
    --photo-cool: #6f7a84;
  }
  * { margin: 0; padding: 0; box-sizing: border-box; }
  html, body {
    width: 1200px; height: 350px; overflow: hidden; background: var(--paper);
  }
  .billboard {
    position: relative; width: 1200px; height: 350px;
    background: linear-gradient(135deg, var(--paper) 0%, var(--paper-soft) 100%);
    overflow: hidden;
  }
  .band-top {
    position: absolute; left: 0; top: 0; width: 988px; height: 8px; background: var(--ink);
  }
  .band-bottom {
    position: absolute; bottom: 0; height: 8px; background: var(--ink);
  }
  .band-bottom.left { left: 0; width: 357px; }
  .band-bottom.right { left: 660px; width: 328px; }
  .side-panel {
    position: absolute; left: 988px; top: 0; width: 212px; height: 350px; background: var(--paper);
  }
  .headline {
    position: absolute; left: 40px; top: 18px; width: 936px; height: 164px;
  }
  .tagline {
    position: absolute; left: 200px; top: 188px; width: 620px; text-align: center;
    font-family: "Open Sans", sans-serif; font-weight: 800; font-size: 38px;
    color: var(--accent-red); letter-spacing: 0.2px; line-height: 1;
  }
  .phone {
    position: absolute; left: 196px; top: 224px; width: 610px; text-align: center;
    font-family: "Open Sans", sans-serif; font-weight: 800; font-size: 90px;
    color: var(--accent-blue); line-height: 1; letter-spacing: 1px;
  }
  .website {
    position: absolute; left: 357px; top: 316px; width: 303px; text-align: center;
    font-family: "Open Sans", sans-serif; font-weight: 800; font-size: 22px;
    color: var(--ink); line-height: 1;
  }
  .portrait {
    position: absolute; width: 136px; height: 136px; border-radius: 50%;
    border: 4px solid var(--accent-blue); background: var(--paper);
    display: flex; align-items: center; justify-content: center;
  }
  .portrait .photo {
    width: 118px; height: 118px; border-radius: 50%;
    background: radial-gradient(circle at 50% 45%, #c9a58a 0%, var(--photo-warm) 55%, #4a3f33 100%);
  }
  .portrait.left { left: 28px; top: 193px; }
  .portrait.right { left: 842px; top: 193px; }
  .award-badge {
    position: absolute; left: 1012px; top: 20px; width: 160px; height: 223px;
    background: var(--accent-blue); padding: 6px;
  }
  .award-badge .inner {
    width: 100%; height: 100%;
    background: linear-gradient(180deg, #5cc6f2 0%, var(--accent-blue) 20%, var(--badge-navy) 34%, var(--badge-navy) 82%, var(--accent-blue) 82%);
  }
  .firm-name {
    position: absolute; left: 1010px; top: 266px; width: 170px;
    display: flex; align-items: center; gap: 8px;
    font-family: "Montserrat", sans-serif; font-weight: 700; font-size: 19px;
    color: var(--ink); line-height: 1.05;
  }
  .firm-name .mark { width: 10px; height: 64px; background: var(--ink); flex: none; }
</style>
</head>
<body>
  <div class="billboard">
    <div class="band-top"></div>
    <div class="side-panel"></div>

    <svg class="headline" viewBox="0 0 936 164" role="img" aria-label="Large word INJURED with letters filled by photographs of injured people, a courthouse, a gavel and a family">
      <defs>
        <linearGradient id="letterFill" x1="0" y1="0" x2="1" y2="0">
          <stop offset="0" stop-color="#b88c74"/>
          <stop offset="0.3" stop-color="#7d7f80"/>
          <stop offset="0.5" stop-color="#9a6a4e"/>
          <stop offset="0.7" stop-color="#6a4a36"/>
          <stop offset="1" stop-color="#5f6b55"/>
        </linearGradient>
      </defs>
      <text x="468" y="156" text-anchor="middle" textLength="928" lengthAdjust="spacingAndGlyphs"
            font-family="'Alfa Slab One', serif" font-size="190"
            fill="url(#letterFill)" stroke="#ffffff" stroke-width="3" paint-order="stroke">INJURED</text>
    </svg>

    <p class="tagline">30+ YEARS OF LITIGATION</p>
    <p class="phone">555-318-4092</p>
    <p class="website">www.kgarnettfirm.example</p>

    <div class="portrait left"><div class="photo" role="img" aria-label="Portrait photo of attorney"></div></div>
    <div class="portrait right"><div class="photo" role="img" aria-label="Portrait photo of attorney"></div></div>

    <div class="award-badge" role="img" aria-label="Community award badge"><div class="inner"></div></div>

    <div class="firm-name">
      <span>Garnett &amp; Lyle<br>Law Firm</span>
      <span class="mark"></span>
    </div>

    <div class="band-bottom left"></div>
    <div class="band-bottom right"></div>
  </div>
</body>
</html>
```